Foodcard Package Design for 10ml Food Enhancer

I have developed a product with a friend that we will be selling later this year, it is a liquid that comes in a small 10ml or 20ml bottle for sale in shops (a flavour enhancer).

A small cardboard sized backer of approximate size "A5" is the best packaging for this product.

i have attached an example of what I am looking for - the front will hold the bottle inside a small plastic case, and the back will be how to use the product / instructions.

What I am looking for is:
Strong graphic design skills to capture customers attention
Good layout of "how to use" instructions so it is clear for customer to understand
Similar "feel" to attached document as guide only

(Note: I will add the words myself, the graphics is all I need. When you design the front & back you will add Lorem ipsom text to display position of text only).

Target Market(s)

Retail & Restaurant industry

Industry/Entity Type

Retail

Font styles to use
Serif

Requirements
Must have
• Captures customers attention, high impact, sophisticated
Nice to have
• Colour, cutting edge look
Should not have
• Not cheap looking

```html
<!DOCTYPE html>
<html lang="en">
<head>
<meta charset="utf-8">
<title>Timber Essence – Blister Card Front and Back</title>
<link rel="stylesheet" href="https://fonts.googleapis.com/css2?family=Arimo:wght@400;700&family=Roboto+Slab:wght@800&display=swap">
<style>
  :root {
    --page: #ffffff;
    --green-edge: #8db32a;
    --green-mid: #b3cf3a;
    --yellow-core: #eef25a;
    --red: #c4141c;
    --brand-red: #b3141c;
    --number-brown: #c0602a;
    --amber: #e3a21e;
    --orange-liquid: #ec8058;
    --ink: #111111;
    --pill-light: #fbfbe6;
    --pill-yellow: #efe23a;
  }
  * { box-sizing: border-box; margin: 0; padding: 0; }
  html, body { width: 1200px; height: 800px; overflow: hidden; background: var(--page); }
  body { font-family: "Arimo", Arial, sans-serif; color: var(--ink); position: relative; }

  .card {
    position: absolute; top: 55px; width: 470px; height: 690px;
    border-radius: 16px; overflow: hidden;
    background:
      radial-gradient(ellipse 60% 55% at 50% 52%, var(--yellow-core) 0%, rgba(238,242,90,0) 100%),
      linear-gradient(180deg, var(--green-edge) 0%, var(--green-mid) 30%, var(--green-mid) 70%, var(--green-edge) 100%);
  }
  .card::before {
    content: ""; position: absolute; inset: 22px; border-radius: 6px;
    background: linear-gradient(90deg, rgba(238,242,90,0.15), rgba(247,243,106,0.75) 50%, rgba(238,242,90,0.15));
  }
  .card--back { left: 118px; }
  .card--front { left: 612px; }

  .hang-hole { position: absolute; left: 50%; top: 28px; transform: translateX(-50%); z-index: 3; }

  .brand {
    position: absolute; left: 0; right: 0; top: 98px; z-index: 3;
    text-align: center; font-family: "Roboto Slab", Georgia, serif; font-weight: 800;
    color: var(--brand-red); line-height: 1;
  }
  .brand__line { display: block; }
  .brand__line--main { font-size: 58px; }
  .brand__line--sub { font-size: 40px; margin-top: 4px; }

  .copy { position: absolute; z-index: 3; font-size: 11px; line-height: 13px; }
  .copy b { font-weight: 700; }
  .copy--center { text-align: center; }

  .step {
    position: absolute; left: 152px; width: 215px; height: 46px; z-index: 3;
    border-radius: 23px;
    background: linear-gradient(90deg, var(--pill-light) 0%, #f6f0a0 50%, var(--pill-yellow) 100%);
    box-shadow: 0 2px 3px rgba(90,110,10,0.35);
  }
  .step__num {
    position: absolute; left: -6px; top: 4px; width: 38px; height: 38px; border-radius: 50%;
    background: var(--number-brown); color: #fff; font-weight: 700; font-size: 26px;
    display: flex; align-items: center; justify-content: center;
    border: 2px solid #fff;
  }
  .step__text { position: absolute; left: 48px; top: 12px; font-size: 8px; line-height: 10px; }

  .art { position: absolute; z-index: 3; background: var(--amber); border-radius: 3px; }
  .art--upright { width: 26px; height: 76px; }
  .art--tilted { width: 74px; height: 24px; transform: rotate(12deg); }

  .bg-art {
    position: absolute; z-index: 2; left: 120px; top: 0; width: 350px; height: 690px;
    background: linear-gradient(180deg, rgba(232,162,26,0.45) 0%, rgba(250,240,60,0.45) 60%, rgba(250,240,60,0.2) 100%);
  }
  .band { position: absolute; z-index: 3; left: 0; top: 330px; width: 428px; height: 40px; background: var(--red); border-radius: 0 20px 20px 0; }
  .band__volume {
    position: absolute; left: 8px; top: 4px; width: 90px; height: 32px; border-radius: 16px;
    background: linear-gradient(90deg, var(--pill-yellow), #f7df2c);
    color: var(--red); font-weight: 700; font-size: 20px;
    display: flex; align-items: center; justify-content: center;
  }
  .tagline { position: absolute; z-index: 3; left: 290px; top: 290px; width: 150px; text-align: center; font-weight: 700; font-size: 11px; line-height: 14px; font-variant: small-caps; }
  .blister {
    position: absolute; z-index: 4; left: 170px; top: 210px; width: 100px; height: 380px;
    border-radius: 14px; border: 2px solid rgba(255,255,255,0.7);
    background: rgba(255,255,255,0.18);
  }
  .blister__product {
    position: absolute; left: 22px; top: 16px; width: 52px; height: 344px; border-radius: 6px;
    background: linear-gradient(90deg, #e6704a, var(--orange-liquid) 50%, #e6704a);
  }
</style>
</head>
<body>

<section class="card card--back">
  <svg class="hang-hole" width="100" height="34" viewBox="0 0 100 34" aria-hidden="true">
    <path d="M15 12 H38 A12 12 0 0 1 62 12 H85 A11 11 0 0 1 85 34 H15 A11 11 0 0 1 15 12 Z" fill="#fff"/>
  </svg>
  <h1 class="brand"><span class="brand__line brand__line--main">Timber</span><span class="brand__line brand__line--sub">Essence</span></h1>
  <p class="copy" style="left:92px; top:215px; width:300px;"><b>Lorem ipsum</b> dolor sit amet, consectetur adipiscing elit, sed do eiusmod tempor incididunt ut labore et dolore magna ullamco laboris nisi ut aliquip ex ea commodo consequat.</p>

  <div class="art art--upright" role="img" aria-label="Illustration: closed vial" style="left:102px; top:258px;"></div>
  <div class="step" style="top:270px;"><span class="step__num">1</span><p class="step__text"><b>Lorem ipsum</b> dolor sit amet, consectetur<br>Ut enim ad minim veniam, quis nostr</p></div>

  <div class="art art--upright" role="img" aria-label="Illustration: vial with cork removed" style="left:388px; top:345px;"></div>
  <div class="step" style="top:353px;"><span class="step__num">2</span><p class="step__text"><b>Lorem ipsum</b> dolor sit amet, consectetur<br>Ut enim ad minim veniam, quis nostr</p></div>

  <div class="art art--tilted" role="img" aria-label="Illustration: vial pouring drops" style="left:56px; top:440px;"></div>
  <div class="step" style="top:437px;"><span class="step__num">3</span><p class="step__text"><b>Lorem ipsum</b> dolor sit amet, consectetur<br>Ut enim ad minim veniam, quis nostr</p></div>

  <div class="art art--upright" role="img" aria-label="Illustration: vial releasing aroma" style="left:388px; top:480px;"></div>
  <div class="step" style="top:520px;"><span class="step__num">4</span><p class="step__text"><b>Lorem ipsum</b> dolor sit amet, consectetur<br>Ut enim ad minim veniam, quis nostr</p></div>

  <p class="copy copy--center" style="left:60px; top:580px; width:350px;"><b>Lorem ipsum</b> dolor sit amet, consectetur adipiscing elit, ullamco laboris nisi ut aliquip ex ea commodo consequat.</p>
  <p class="copy copy--center" style="left:60px; top:615px; width:350px;"><b>Lorem ipsum</b> dolor sit amet,<br>consectetur adipiscing elit, sed do eiusmod tempor incididunt aliqua.</p>
</section>

<section class="card card--front">
  <div class="bg-art" role="img" aria-label="Decorative illustration of amber and yellow bottles"></div>
  <svg class="hang-hole" width="100" height="34" viewBox="0 0 100 34" aria-hidden="true">
    <path d="M15 12 H38 A12 12 0 0 1 62 12 H85 A11 11 0 0 1 85 34 H15 A11 11 0 0 1 15 12 Z" fill="#fff"/>
  </svg>
  <h1 class="brand"><span class="brand__line brand__line--main">Timber</span><span class="brand__line brand__line--sub">Essence</span></h1>
  <p class="tagline">Lorem ipsum dolor<br>commodo consequat</p>
  <div class="band"><span class="band__volume">10 mL</span></div>
  <p class="copy" style="left:45px; top:390px; width:110px;"><b>Lorem ipsum</b> dolor sit amet, consectetur adipiscing elit, sed do eiusmod tempor incididunt ut labore et dolore magna ullamco laboris nisi ut aliquip ex ea commodo consequat.</p>
  <div class="blister">
    <div class="blister__product" role="img" aria-label="Photo: 10 mL glass vial with cork and orange liquid"></div>
  </div>
  <p class="copy copy--center" style="left:60px; top:602px; width:350px;"><b>Lorem ipsum</b> dolor sit amet, consectetur adipiscing elit, ullamco laboris nisi ut aliquip ex ea commodo consequat.</p>
  <p class="copy copy--center" style="left:60px; top:662px; width:350px;"><b>Lorem ipsum</b> dolor sit amet,<br>consectetur adipiscing elit, sed do eiusmod tempor incididunt aliqua.</p>
</section>

</body>
</html>
```